Design a nice looking size chart

Please design a nice looking size chart for swim parkas. Please include company logo in attached. Please see attached image of sizing information. Also include XX-Small. Chest: 44"-45.5" Sleeve Length: 29.5" Parka Length: 40.75"

```html
<!DOCTYPE html>
<html lang="en">
<head>
<meta charset="utf-8">
<title>Swim Parka Size Chart</title>
<link rel="stylesheet" href="https://fonts.googleapis.com/css2?family=Jost:wght@400;500&family=Open+Sans:wght@400&display=swap">
<style>
  :root {
    --backdrop: #333333;
    --sheet: #ffffff;
    --brand-red: #e31b2b;
    --ink: #111111;
    --label-ink: #222222;
  }
  html, body {
    margin: 0;
    padding: 0;
    width: 1200px;
    height: 848px;
    overflow: hidden;
    background: var(--backdrop);
  }
  .canvas {
    position: relative;
    width: 1200px;
    height: 848px;
    background: var(--backdrop);
  }
  .size-sheet {
    position: absolute;
    left: 177px;
    top: 258px;
    width: 869px;
    height: 256px;
    background: var(--sheet);
  }
  .brand {
    position: absolute;
    left: 24px;
    top: 26px;
    width: 100px;
    display: flex;
    flex-direction: column;
    align-items: center;
    gap: 6px;
  }
  .brand-dot {
    width: 40px;
    height: 40px;
    border-radius: 50%;
    background: var(--brand-red);
  }
  .brand-name {
    font-family: "Jost", sans-serif;
    font-weight: 500;
    font-size: 19px;
    letter-spacing: 1px;
    color: var(--ink);
    line-height: 1;
  }
  .sheet-title {
    position: absolute;
    right: 29px;
    top: 18px;
    margin: 0;
    font-family: "Jost", sans-serif;
    font-weight: 500;
    font-size: 44px;
    line-height: 1;
    letter-spacing: 0.5px;
    color: var(--ink);
  }
  .size-table {
    position: absolute;
    left: 10px;
    top: 64px;
    display: grid;
    grid-template-columns: 112px repeat(7, 99px);
    column-gap: 4px;
    row-gap: 0;
  }
  .size-head {
    height: 37px;
    background: var(--brand-red);
    color: #ffffff;
    font-family: "Open Sans", sans-serif;
    font-size: 12px;
    display: flex;
    align-items: center;
    justify-content: center;
  }
  .corner { background: none; }
  .cell {
    position: relative;
    height: 40px;
    display: flex;
    align-items: flex-end;
    justify-content: center;
    padding-bottom: 10px;
    box-sizing: border-box;
    font-family: "Open Sans", sans-serif;
    font-size: 11.5px;
    color: var(--label-ink);
  }
  .cell::after {
    content: "";
    position: absolute;
    left: 0;
    right: 0;
    bottom: 2px;
    height: 5px;
    border: 1px solid var(--brand-red);
    border-top: none;
  }
  .row-label { color: var(--ink); }
</style>
</head>
<body>
<div class="canvas">
  <section class="size-sheet">
    <div class="brand">
      <span class="brand-dot"></span>
      <span class="brand-name">KELPRO</span>
    </div>
    <h1 class="sheet-title">SIZE CHART</h1>

    <div class="size-table">
      <div class="corner"></div>
      <div class="size-head">XX-Small</div>
      <div class="size-head">X-Small</div>
      <div class="size-head">Small</div>
      <div class="size-head">Medium</div>
      <div class="size-head">Large</div>
      <div class="size-head">X-Large</div>
      <div class="size-head">2X-Large</div>

      <div class="cell row-label">Chest</div>
      <div class="cell">44″ - 45.5″</div>
      <div class="cell">45″ - 46.5″</div>
      <div class="cell">46.5″ - 48″</div>
      <div class="cell">47.5″ - 49.5″</div>
      <div class="cell">49.5″ - 51″</div>
      <div class="cell">51″ - 52.5″</div>
      <div class="cell">52.5″ - 55″</div>

      <div class="cell row-label">Sleeve Length</div>
      <div class="cell">29.5″</div>
      <div class="cell">30″</div>
      <div class="cell">30.5″</div>
      <div class="cell">31″</div>
      <div class="cell">32″</div>
      <div class="cell">33″</div>
      <div class="cell">34.75″</div>

      <div class="cell row-label">Parka Length</div>
      <div class="cell">40.75″</div>
      <div class="cell">42″</div>
      <div class="cell">42.5″</div>
      <div class="cell">42.75″</div>
      <div class="cell">44″</div>
      <div class="cell">44.5″</div>
      <div class="cell">45.75″</div>
    </div>
  </section>
</div>
</body>
</html>
```